a simple functional website for an up and coming service industry business

hi ,i also require in store promotional items like business cards, flyers, plain square page t-shirts for workers and want all these to have the same look and feel.i need my website to catch the eye .the idea i have in my head is something that will sell the service ,the website is a tool to get people to inquire , book or pay for an assembly service.we assemble flatpack furniture , outdoor furniture,playgrounds etc ,basically anything that comes with instructions,our biggest customer at the moment is vormbo who we assemble nationally.i am looking for a website to be bright modern and simple to use the current website is www.pelmarbuildcrew.com which is dull with to many pages . i have already had a new logo designed by sketch harbor and it is lime green and sky blue in colour, a webiste i like is taskly q4 although it has lots of flash and my budget probably wouldn't allow that at the moment.

Target Market(s)

customer will be visiting the website to find out about the service we provide , then hopefully making contact,either booking a job or asking for a quote, i like the idea of the phone, email icons on the home screen

Industry/Entity Type

Industry

Requirements
Must have
• a contact icon: when you click on it the page with the name ,email address ,phone number, address pops up

a phone icon : when you click on it the 1300 number pops up
Nice to have
• my current website is with pagr and it is www.pelmarbuildcrew.com

a website i really like the design of is taskly q4 and vormbo

would like some pictures of modern furniture ,bbq's ,gym equipment ,playground equiptment
Should not have
• the career page or price page my current website .i don't want it on there anymore

```html
<!DOCTYPE html>
<html lang="en">
<head>
<meta charset="utf-8">
<title>Pelmar Build Crew – Flat Pack Assembly</title>
<link href="https://fonts.googleapis.com/css2?family=Ubuntu:wght@400;500;700&family=Carlito:wght@400;700&display=swap" rel="stylesheet">
<style>
:root{
  --lime:#8cc63f;
  --lime-dark:#6ea92a;
  --sky:#1a8ad4;
  --sky-dark:#0f6fb3;
  --text:#2b2b2b;
  --muted:#8a8a8a;
  --pale-blue:#e3f1fa;
  --line:#dcdcdc;
  --footer:#3b3b3b;
}
*{box-sizing:border-box;margin:0;padding:0}
html,body{width:1183px;height:1200px;overflow:hidden;background:#fff}
body{position:relative;font-family:"Carlito",sans-serif;color:var(--text)}
.abs{position:absolute}

/* header */
.brand{left:173px;top:60px;display:flex;align-items:center;gap:8px;font-family:"Ubuntu",sans-serif;font-weight:500;font-size:19px;color:var(--lime-dark);letter-spacing:.3px}
.brand-dot{width:34px;height:34px;border-radius:50%;background:var(--sky)}
.phone-box{left:562px;top:19px;width:273px;height:53px;border:1px solid #cfcfcf;border-radius:5px;background:linear-gradient(#fff,#ececec);display:flex;align-items:center;gap:14px;padding-left:18px}
.phone-number{font-family:"Ubuntu",sans-serif;font-weight:700;font-size:25px;color:var(--sky-dark);letter-spacing:1px}
.social{left:856px;top:27px;display:flex;gap:7px}
.social span{width:34px;height:35px;border-radius:3px;background:var(--sky)}
.social span:nth-child(2){background:var(--lime)}
.main-nav{left:652px;top:90px;height:33px}
.main-nav a{position:absolute;top:0;height:33px;line-height:37px;text-align:center;color:#fff;text-decoration:none;font-family:"Ubuntu",sans-serif;font-weight:500;font-size:15px;letter-spacing:.8px;border-radius:5px 5px 0 0;background:linear-gradient(#2a9be6,var(--sky-dark))}
.main-nav a.active{background:linear-gradient(#9fd24f,var(--lime-dark))}
.top-rule{left:0;top:122px;width:1183px;height:2px;background:var(--sky)}

/* hero band */
.hero-band{left:0;top:124px;width:1183px;height:451px;background:var(--pale-blue)}
.slider-frame{left:169px;top:139px;width:845px;height:289px;background:#fff;padding:5px}
.slide{width:100%;height:100%;background:linear-gradient(135deg,#3a3530 0%,#6b5a48 45%,#b49a78 70%,#e6e0d8 100%)}
.slider-dots{left:560px;top:407px;display:flex;gap:8px}
.slider-dots span{width:10px;height:10px;background:#222}
.slider-dots span:first-child{background:var(--sky)}
.category{top:439px;width:267px;height:136px;border-radius:134px 134px 0 0;border:4px solid #fff;border-bottom:0;overflow:hidden}
.category .photo{position:absolute;inset:0}
.category .label{position:absolute;left:0;right:0;bottom:0;height:32px;background:rgba(26,120,190,.85);color:#fff;text-align:center;font-family:"Ubuntu",sans-serif;font-weight:500;font-size:19px;line-height:32px;letter-spacing:.6px}

/* welcome */
.welcome-title{left:175px;top:585px;font-family:"Ubuntu",sans-serif;font-weight:500;font-size:18px;color:var(--lime-dark)}
.welcome-title b{color:var(--sky-dark);font-weight:500}
.dashed{left:175px;top:618px;width:830px;border-top:1px dashed #cfcfcf}
.intro{left:175px;top:628px;width:592px;font-size:14.4px;line-height:15.3px;text-align:justify}
.intro p{margin-bottom:15.3px}
.intro .name{color:var(--sky-dark);font-weight:700}
.intro .call{color:var(--lime-dark)}
.intro-photo{left:787px;top:635px;width:217px;height:155px;border:3px solid #fff;box-shadow:0 0 0 1px #ddd;background:linear-gradient(120deg,#3a2a22,#7a5a40 50%,#d9cdb8 80%,#3c2a24)}
.separator{left:169px;top:811px;width:845px;height:2px;background:#e4e4e4}

/* service lists */
.service-list{top:830px;width:197px;border:1px solid #ddd}
.service-list h3{height:31px;background:linear-gradient(#9fd24f,var(--lime-dark));color:#fff;font-family:"Ubuntu",sans-serif;font-weight:400;font-size:16px;line-height:32px;padding-left:13px}
.service-list li{list-style:none;height:32.6px;line-height:33px;padding-left:8px;font-size:14px;background:linear-gradient(#fff,#efefef)}
.service-list li::before{content:"• "}

.help-title{left:608px;top:827px;font-family:"Ubuntu",sans-serif;font-weight:400;font-size:18px;color:var(--sky-dark)}
.feature{width:195px;height:47px;border:1px solid #d6d6d6;border-radius:24px;background:linear-gradient(#fff,#ececec);display:flex;align-items:center;gap:8px;padding-left:4px;font-family:"Ubuntu",sans-serif;font-weight:500;color:#333;font-size:15px;line-height:15px}
.feature.small{font-size:12.5px}
.feature i{flex:none;width:39px;height:39px;border-radius:50%;background:radial-gradient(circle at 40% 35%,#3aa7ee,var(--sky-dark));border:2px solid #fff;box-shadow:0 0 0 1px #bbb}

/* enquiry form */
.form-band{left:0;top:1042px;width:1183px;height:84px;background:#eeeeee}
.field{height:30px;border:1px solid #ccc;border-bottom:3px solid #aaa;border-radius:4px;background:#fff;font-size:11px;color:var(--muted);padding:7px 10px}
.submit{left:917px;top:1071px;width:96px;height:36px;border:1px solid #bbb;border-bottom:3px solid #999;border-radius:4px;background:linear-gradient(#fff,#e6e6e6);font-family:"Ubuntu",sans-serif;font-weight:500;font-size:14px;text-align:center;line-height:32px}

/* footer */
.footer{left:0;top:1136px;width:1183px;height:64px;background:var(--footer)}
.footer-brand{left:177px;top:1177px;font-family:"Ubuntu",sans-serif;font-size:9px;color:#6a6a6a}
.footer-nav{left:0;width:1290px;top:1148px;display:flex;justify-content:center;font-family:"Ubuntu",sans-serif;font-size:10.5px;letter-spacing:1px;color:#fff}
.footer-nav span{padding:0 12px;border-left:1px solid #777}
.footer-nav span:first-child{border-left:0}
.copyright{left:0;width:1290px;top:1174px;text-align:center;font-size:11px;color:#ddd}
</style>
</head>
<body>

<div class="abs brand"><span class="brand-dot"></span>PELMAR BUILD CREW</div>

<div class="abs phone-box">
  <svg width="38" height="34" viewBox="0 0 38 34" aria-hidden="true">
    <path d="M3 11 Q19 -2 35 11 L31 16 L25 13 L25 9 Q19 6 13 9 L13 13 L7 16 Z" fill="#555"/>
    <path d="M10 15 L28 15 L33 31 L5 31 Z" fill="#555"/>
    <circle cx="19" cy="23" r="5" fill="#eee"/><circle cx="19" cy="23" r="2" fill="#555"/>
  </svg>
  <span class="phone-number">1300-555-018</span>
</div>

<div class="abs social" aria-label="Social links"><span></span><span></span><span></span><span></span></div>

<nav class="abs main-nav">
  <a class="active" href="#" style="left:0;width:107px">HOME</a>
  <a href="#" style="left:110px;width:132px">SERVICES</a>
  <a href="#" style="left:245px;width:116px">CONTACT</a>
</nav>
<div class="abs top-rule"></div>

<div class="abs hero-band"></div>
<div class="abs slider-frame"><div class="slide" role="img" aria-label="Modern kitchen with dark cabinets and a bench set with fresh fruit"></div></div>
<div class="abs slider-dots"><span></span><span></span><span></span><span></span></div>

<div class="abs category" style="left:172px"><div class="photo" role="img" aria-label="Bright open-plan office with desks and green chairs" style="background:linear-gradient(#e9ecec,#b9c6c0 60%,#8ea08e)"></div><div class="label">Indoore Furniture</div></div>
<div class="abs category" style="left:457px"><div class="photo" role="img" aria-label="White modern kitchen with pendant lights" style="background:linear-gradient(#f3f3f3,#cfd3d6 60%,#9fa8ad)"></div><div class="label">Outdoor Furniture</div></div>
<div class="abs category" style="left:744px"><div class="photo" role="img" aria-label="Outdoor timber dining setting on a lit patio" style="background:linear-gradient(#2f3d2a,#6a5838 55%,#a7825a)"></div><div class="label">Gym’s</div></div>

<h1 class="abs welcome-title">Welcome to <b>PELMAR BUILD CREW</b></h1>
<div class="abs dashed"></div>
<div class="abs intro">
  <p><span class="name">&nbsp;Pelmar Build Crew &amp; Installation</span> are the ready to assemble fit out specialists. We assemble and install DIY flat pack indoor and outdoor furniture, across South East Queensland for the major retailers.</p>
  <p>We provide a reliable domestic or commercial service with professional and qualified installers.</p>
  <p>With the necessary builders licence, insurances and over 10 years experience in how to install, at Pelmar Build Crew &amp; Installation we make the job easy for you.</p>
  <p><span class="call">CALL 1300 555 018</span> to discuss your requirements and one of our prompt installers will contact you in a jiffy.</p>
</div>
<div class="abs intro-photo" role="img" aria-label="Modern bedroom with brick feature wall, wardrobe and striped bed"></div>
<div class="abs separator"></div>

<div class="abs service-list" style="left:172px">
  <h3>Commercial Fit Out</h3>
  <ul><li>Office</li><li>Interior Designer fit out</li><li>Hotel</li><li>Display home</li><li>Kitchen</li></ul>
</div>
<div class="abs service-list" style="left:386px">
  <h3>Domestic Fits Out</h3>
  <ul><li>Indoor furniture</li><li>Outdoor Furniture</li><li>Playgrounds</li><li>BBQ’s</li><li>Gyms</li></ul>
</div>

<h2 class="abs help-title">How Can We Help Your assembly service</h2>
<div class="abs feature" style="left:602px;top:864px"><i></i>Reliability</div>
<div class="abs feature" style="left:814px;top:864px"><i></i>Efficiency</div>
<div class="abs feature" style="left:602px;top:921px"><i></i>Flexibility</div>
<div class="abs feature small" style="left:814px;top:921px"><i></i>Excellent<br>Communication</div>
<div class="abs feature small" style="left:602px;top:978px"><i></i>Personal<br>Shopper / Delivery</div>
<div class="abs feature" style="left:814px;top:978px"><i></i>Handman Services</div>

<div class="abs form-band"></div>
<div class="abs field" style="left:172px;top:1054px;width:207px">Your Name :</div>
<div class="abs field" style="left:390px;top:1054px;width:207px">Phone No :</div>
<div class="abs field" style="left:172px;top:1093px;width:207px">Email Address :</div>
<div class="abs field" style="left:390px;top:1093px;width:207px">Location :</div>
<div class="abs field" style="left:608px;top:1054px;width:291px;height:69px">Message :</div>
<div class="abs submit">Submit</div>

<footer class="abs footer"></footer>
<div class="abs footer-brand">PELMAR BUILD CREW</div>
<div class="abs footer-nav"><span>HOME</span><span>SERVICES</span><span>CONTACT</span><span>SITEMAP</span><span>PRIVACY POLICY</span><span>TERMS&amp;CONDITION</span></div>
<div class="abs copyright">© Copyright 2013 PELMAR BUILD CREW PTY LTD</div>

</body>
</html>
```